Church Bulletin Ad (see attached sample)

Create a New Church Bulletin Ad. I have attached some samples of what we would like to have in the ad. (1) Marrowfield Realty Thorne Logo (2) Headshot (3) Lena Vasko & Greta Vasko, Real Estate Team (4) Phone number (5) Email address (6) St Aldwin Parishioners for over 40 Years. We would like for the ad to be clean and modern. NO OTHER IMAGES besides headshots and Marrowfield Realty Thorne Logo.

Target Market(s)

Church community

Industry/Entity Type

Real Estate

Font styles to use
Sans Serif
Other font styles liked:
• Modern Font

Colors
0054AA
0677BA
7BADD7
CADEEF
E8F1F8

Requirements
Must have
• Marrowfield Realty Thorne Logo; Headshot; Ad size is 4.5"x1.62"

```html
<!DOCTYPE html>
<html lang="en">
<head>
<meta charset="utf-8">
<title>Lena Vasko &amp; Greta Vasko Real Estate Team – Bulletin Ad</title>
<link href="https://fonts.googleapis.com/css2?family=Lato:wght@400;700;900&display=swap" rel="stylesheet">
<style>
  :root {
    --navy: #0d3358;
    --navy-text: #163a5f;
    --teal: #1a5a80;
    --headline: #1c5a7e;
    --panel: #e5e6e7;
    --sky-top: #a9c3d6;
    --sky-bottom: #ffffff;
    --frame: #111111;
    --shadow: #e0e0e0;
    --white: #ffffff;
  }
  * { box-sizing: border-box; margin: 0; padding: 0; }
  html, body { width: 1200px; height: 515px; overflow: hidden; background: var(--white); }
  body { font-family: "Lato", sans-serif; }

  .canvas {
    position: relative; width: 1200px; height: 515px;
    border: 1.5px solid var(--frame); background: var(--white);
  }
  .ad-shadow {
    position: absolute; left: 78px; top: 68px; width: 1080px; height: 390px;
    background: var(--shadow);
  }
  .ad {
    position: absolute; left: 66px; top: 53px; width: 1080px; height: 388px;
    background: linear-gradient(to bottom, var(--sky-top), var(--sky-bottom) 60%);
    border: 1px solid #c9c9c9; overflow: hidden;
  }
  .ad-shapes { position: absolute; inset: 0; }

  .headshot { position: absolute; }
  .headshot--left {
    left: 0; top: 63px; width: 226px; height: 270px;
    background: linear-gradient(to bottom, #6b4a3a 0%, #c79a86 35%, #f2f2f2 62%, #1f1f1f 78%);
    border-radius: 110px 110px 0 0;
  }
  .headshot--right {
    left: 861px; top: 59px; width: 219px; height: 274px;
    background: linear-gradient(to bottom, #ece9e4 0%, #e7c2ae 40%, #4a4540 70%, #2d2a28 100%);
    border-radius: 105px 105px 0 0;
  }

  .brand {
    position: absolute; left: 359px; top: 28px; width: 117px; height: 110px;
    background: var(--navy); color: var(--white);
    display: flex; align-items: center; justify-content: center; text-align: center;
    font-weight: 700; font-size: 15px; line-height: 1.25; padding: 8px;
  }
  .tagline {
    position: absolute; left: 481px; top: 27px;
    color: var(--headline); font-weight: 900; font-size: 37px; line-height: 39px;
    letter-spacing: 0.5px;
  }
  .team-names {
    position: absolute; left: 0; width: 1080px; top: 165px; text-align: center;
    color: var(--navy-text); font-weight: 900; font-size: 32px; line-height: 34px;
    letter-spacing: 0.4px;
  }
  .team-label {
    position: absolute; left: 280px; width: 518px; top: 206px; height: 34px;
    display: flex; align-items: center; gap: 4px;
    color: var(--navy-text); font-size: 29px; line-height: 34px;
  }
  .team-label::before, .team-label::after {
    content: ""; flex: 1; height: 2px; background: var(--navy-text);
  }

  .contact {
    position: absolute; top: 267px; height: 34px; border-radius: 17px;
    background: var(--navy); color: var(--white);
    display: flex; align-items: center; font-size: 19px; line-height: 1;
  }
  .contact--phone { left: 252px; width: 218px; }
  .contact--email { left: 484px; width: 344px; }
  .contact-icon {
    width: 27px; height: 27px; margin: 0 12px 0 3px; border-radius: 50%;
    background: var(--white); display: flex; align-items: center; justify-content: center;
  }
  .contact--email .contact-text { margin-left: 20px; }

  .parish-line {
    position: absolute; left: 0; width: 1080px; top: 321px; height: 67px;
    display: flex; align-items: center; justify-content: center;
    color: var(--white); font-weight: 700; font-size: 27px; line-height: 1;
  }
</style>
</head>
<body>
<div class="canvas">
  <div class="ad-shadow"></div>
  <div class="ad">
    <svg class="ad-shapes" width="1080" height="388" viewBox="0 0 1080 388">
      <polygon points="306,0 773,0 865,333 235,333" fill="var(--panel)"/>
      <rect x="0" y="333" width="1080" height="55" fill="var(--navy)"/>
      <polygon points="224,320 856,320 872,388 208,388" fill="var(--panel)"/>
      <polygon points="247,320 833,320 852,388 227,388" fill="var(--teal)"/>
    </svg>

    <div class="headshot headshot--left" role="img" aria-label="Headshot of Lena Vasko"></div>
    <div class="headshot headshot--right" role="img" aria-label="Headshot of Greta Vasko"></div>

    <div class="brand">Marrowfield Realty Thorne</div>
    <div class="tagline">ENERGY<br>EXCELLENCE<br>EXPERIENCE</div>

    <div class="team-names">LENA VASKO &amp; GRETA VASKO</div>
    <div class="team-label">Real Estate Team</div>

    <div class="contact contact--phone">
      <span class="contact-icon">
        <svg width="16" height="16" viewBox="0 0 24 24"><path fill="var(--navy)" d="M6.6 10.8a15.1 15.1 0 0 0 6.6 6.6l2.2-2.2a1 1 0 0 1 1-.25 11.4 11.4 0 0 0 3.6.57 1 1 0 0 1 1 1V20a1 1 0 0 1-1 1A17 17 0 0 1 3 4a1 1 0 0 1 1-1h3.5a1 1 0 0 1 1 1c0 1.25.2 2.45.57 3.57a1 1 0 0 1-.25 1z"/></svg>
      </span>
      <span class="contact-text">(206) 555-0147</span>
    </div>
    <div class="contact contact--email">
      <span class="contact-icon">
        <svg width="15" height="12" viewBox="0 0 20 15"><rect x="0" y="0" width="20" height="15" rx="2" fill="var(--navy)"/><path d="M1 1.5 10 8.5 19 1.5" stroke="var(--white)" stroke-width="1.8" fill="none"/></svg>
      </span>
      <span class="contact-text">VaskoTeam@MarrowfieldRT.com</span>
    </div>

    <div class="parish-line">St Aldwin Parishioners for over 40 Years</div>
  </div>
</div>
</body>
</html>
```